Design NEW business card

We would like a business card using the colour deep red wine or dark navy blue textured background (patterned or not, open to suggestions) with a high gloss debossed rose gold/copper MT Martin Tully Jewellery business name (Provided). I have included images for your review we would like to keep our currently logo and business name on the front but you can change the layout and positioning. For the back of the card we are open to all suggestions/variations.
Industry/Entity Type
Business
Contact Information for Business Card
Use our current MT Martin Tully Jewellery logo (Provided image)
Look and feel
Each slider illustrates characteristics of the customer's brand and the style your logo design should communicate.

```html
<!DOCTYPE html>
<html lang="en">
<head>
<meta charset="UTF-8">
<title>Martin Tully Jewellery – Business Card</title>
<link href="https://fonts.googleapis.com/css2?family=Open+Sans:wght@400;600&display=swap" rel="stylesheet">
<style>
  :root {
    --stage: #000000;
    --navy: #141c33;
    --navy-deep: #0d1326;
    --wine: #4a0f1c;
    --wine-deep: #350a14;
    --rose-gold: #c99a7c;
    --rose-gold-soft: #b98a6e;
    --ink-light: #e6e1dc;
  }
  * { margin: 0; padding: 0; box-sizing: border-box; }
  html, body {
    width: 1200px; height: 900px; overflow: hidden;
    background: var(--stage);
    font-family: "Open Sans", Arial, sans-serif;
  }
  .stage { position: relative; width: 1200px; height: 900px; }

  .card { position: absolute; top: 200px; width: 310px; height: 502px; overflow: hidden; }
  .card--front {
    left: 265px;
    border-radius: 70px 0 70px 0;
    background:
      repeating-linear-gradient(45deg, rgba(255,255,255,0.025) 0 1px, transparent 1px 6px),
      repeating-linear-gradient(-45deg, rgba(0,0,0,0.18) 0 1px, transparent 1px 6px),
      radial-gradient(circle at 30% 20%, var(--navy), var(--navy-deep));
  }
  .card--back {
    left: 641px;
    border-radius: 0 70px 0 70px;
    background:
      repeating-linear-gradient(45deg, rgba(255,255,255,0.025) 0 1px, transparent 1px 6px),
      repeating-linear-gradient(-45deg, rgba(0,0,0,0.2) 0 1px, transparent 1px 6px),
      radial-gradient(circle at 40% 40%, var(--wine), var(--wine-deep));
  }

  .brand { position: absolute; text-align: right; color: var(--rose-gold); }
  .brand__name {
    display: block;
    font-weight: 400;
    font-size: 17px;
    letter-spacing: 3.2px;
    line-height: 22px;
    text-transform: uppercase;
  }
  .brand__trade {
    display: block;
    font-weight: 400;
    font-size: 7.5px;
    letter-spacing: 10.5px;
    line-height: 12px;
    margin-top: 4px;
    margin-right: -10px;
    text-transform: uppercase;
    color: var(--rose-gold-soft);
  }
  .card--front .brand { right: 15px; top: 160px; }
  .card--back .brand { right: 51px; top: 270px; }

  .contact { position: absolute; left: 27px; top: 326px; color: var(--ink-light); }
  .contact__name {
    color: var(--rose-gold); font-weight: 600; font-size: 17px;
    letter-spacing: 0.2px; text-transform: uppercase; line-height: 22px;
  }
  .contact__role { font-size: 13.5px; line-height: 20px; margin-top: 1px; }
  .contact__address { font-size: 13.5px; line-height: 16px; margin-top: 17px; }
  .contact__lines { list-style: none; margin-top: 11px; font-size: 13.5px; }
  .contact__lines li { display: flex; align-items: center; height: 19px; }
  .contact__icon { width: 10px; height: 10px; margin-right: 6px; fill: var(--rose-gold); }
</style>
</head>
<body>
<main class="stage">
  <section class="card card--front">
    <p class="brand">
      <span class="brand__name">Martin Tully</span>
      <span class="brand__trade">Jewellery</span>
    </p>
    <div class="contact">
      <h1 class="contact__name">Owen Hartley</h1>
      <p class="contact__role">Managing Director</p>
      <p class="contact__address">48 Harbour Lane<br>Westbridge, 204518</p>
      <ul class="contact__lines">
        <li>
          <svg class="contact__icon" viewBox="0 0 10 10" aria-hidden="true">
            <path d="M1 3.2 Q5 0.8 9 3.2 L8.2 4.4 L6.6 3.8 L6.4 3 Q5 2.6 3.6 3 L3.4 3.8 L1.8 4.4 Z"/>
            <rect x="2.2" y="5" width="5.6" height="4" rx="0.6"/>
          </svg>
          555-013-2468
        </li>
        <li>
          <svg class="contact__icon" viewBox="0 0 10 10" aria-hidden="true">
            <rect x="0.5" y="2" width="9" height="6.5" rx="0.6"/>
            <path d="M0.8 2.4 L5 5.6 L9.2 2.4" fill="none" stroke="#141c33" stroke-width="0.9"/>
          </svg>
          hello@martintully.example
        </li>
      </ul>
    </div>
  </section>

  <section class="card card--back">
    <p class="brand">
      <span class="brand__name">Martin Tully</span>
      <span class="brand__trade">Jewellery</span>
    </p>
  </section>
</main>
</body>
</html>
```